Web Site Design for a Finance (lending) Company

We are opening a new subsidiary that focuses on lending money in the real estate industry. We need a web site designed to represent the business.

The business is lending money to real estate investors. A typical client/borrower will be looking to borrow money to buy a house, renovate it and then sell it at a profit, all within 12 months or less.

Company name is Brevand Finance. Our logo is attached.

Attached is a general outline for the web site. We're working on writing more text for each page but this should give you enough to get started with some ideas.

Competitor web site that I like a lot (as an example): https://quorvelfunding.com/. Many of the general items on this site match what we will need (description of loan programs, FAQ)

Target Market(s)

Real estate investors (generally individuals or small companies with just a few people) who are buying homes, renovating them and then selling them at a profit.

Industry/Entity Type

Finance

Coding

Coded - Design and coding required

Number of Pages Required

5+ page

Colors

Designer to choose colors to be used in the design.

Requirements
Must have
• Minimalist design. Clean lines without too much clutter. Some stock photography is ok but the photos should not be distracting. They should almost fade in to the background so that user can focus on the key information about what our company does instead. We are a finance company, not a design company, so the information about our products will be more interesting to site visitors than the art.
• Some minimalist examples from Snapboard:
• https://www.snapboard-example.com/explore/minimalist-web-design/
Nice to have
• If you search in seekly for "hard money lenders" you will find many examples of web sites from our competition. I have provided a link above to competitor web site that I like a lot.
• I have attached our logo in EPS format. Logo is green. Web site doesn't have to be green but it should be of a color that will work well with the logo.

```html
<!DOCTYPE html>
<html lang="en">
<head>
<meta charset="utf-8">
<title>Brevand Finance — Real Estate Lending</title>
<link href="https://fonts.googleapis.com/css2?family=Questrial&family=Jura:wght@400;500&display=swap" rel="stylesheet">
<style>
:root{
  --ink:#111111;
  --brand-green:#1f5a2e;
  --accent:#a57436;
  --accent-overlay:rgba(160,110,50,0.88);
  --white:#ffffff;
  --text:#333333;
  --hero-a:#6f9a4c;
  --hero-b:#9cbf86;
  --hero-c:#5f8a56;
}
*{box-sizing:border-box;margin:0;padding:0}
html,body{width:1040px;height:1200px;overflow:hidden;background:var(--white)}
body{position:relative;font-family:"Jura",sans-serif;color:var(--text)}
.site-header{position:absolute;left:0;top:0;width:1040px;height:68px;background:var(--white)}
.brand{position:absolute;left:52px;top:22px;display:flex;align-items:center;gap:8px;font-family:"Questrial",sans-serif;font-size:17px;color:var(--brand-green)}
.brand-mark{width:14px;height:14px;background:var(--brand-green)}
.main-nav{position:absolute;right:52px;top:25px;display:flex;gap:21px;font-family:"Questrial",sans-serif;font-size:14px;letter-spacing:1px;color:var(--ink)}
.main-nav a{color:inherit;text-decoration:none;position:relative}
.main-nav a.active::after{content:"";position:absolute;left:7px;right:7px;bottom:-3px;height:1px;background:var(--ink)}
.hero{position:absolute;left:0;top:68px;width:1040px;height:543px;background:linear-gradient(160deg,var(--hero-a) 0%,var(--hero-b) 45%,var(--hero-c) 100%)}
.hero-bracket{position:absolute;left:130px;top:126px;width:58px;height:152px;border-left:10px solid var(--white);border-bottom:10px solid var(--white);border-bottom-left-radius:6px}
.hero-title{position:absolute;left:166px;top:118px;font-family:"Jura",sans-serif;font-weight:500;font-size:39px;line-height:48px;letter-spacing:7px;color:var(--white)}
.hero-lede{position:absolute;left:202px;top:264px;width:720px;font-size:17.5px;line-height:25px;letter-spacing:3px;color:var(--white)}
.scroll-down{position:absolute;left:496px;top:473px;width:48px;height:70px;background:var(--accent);display:flex;justify-content:center;padding-top:18px}
.section-title{position:absolute;left:0;top:690px;width:1040px;text-align:center;font-family:"Questrial",sans-serif;font-size:38px;letter-spacing:8px;color:var(--ink)}
.divider{position:absolute;left:432px;top:744px;width:176px;height:18px}
.company-heading{position:absolute;left:52px;top:922px;font-family:"Questrial",sans-serif;font-size:36px;line-height:48px;letter-spacing:7px;color:var(--ink)}
.company-heading .accent{color:var(--accent)}
.company-copy{position:absolute;left:52px;top:1028px;width:430px;font-size:14.5px;line-height:17.4px;letter-spacing:1.6px;color:var(--text)}
.mission-photo{position:absolute;left:519px;top:850px;width:521px;height:221px;background:linear-gradient(120deg,#3e3e3e,#8a8a88 50%,#4a4a4a)}
.mission-card{position:absolute;left:538px;top:858px;width:484px;height:206px;background:var(--accent-overlay);color:var(--white);text-align:center;padding-top:42px}
.mission-card h3{font-family:"Jura",sans-serif;font-weight:500;font-size:18px;letter-spacing:2.5px;margin-bottom:5px}
.mission-card p{width:340px;margin:0 auto;font-size:11.5px;line-height:13.4px;letter-spacing:1px}
.mission-card .more{position:absolute;right:80px;top:188px;top:auto;bottom:26px;font-size:12px;letter-spacing:1.2px;color:var(--white);text-decoration:none}
.tile{position:absolute;top:1071px;height:129px}
.tile-target{left:519px;width:261px;background:linear-gradient(135deg,#cfcfcb,#8c8c86)}
.tile-arrows{left:780px;width:260px;background:linear-gradient(135deg,#6d6d6b,#4a4a48 60%,#9a8a3a)}
</style>
</head>
<body>
<header class="site-header">
  <div class="brand"><span class="brand-mark"></span>Brevand Finance</div>
  <nav class="main-nav">
    <a class="active" href="#">HOME</a>
    <a href="#">ABOUT US</a>
    <a href="#">LOANS</a>
    <a href="#">RESOURCES</a>
    <a href="#">CONTACT US</a>
  </nav>
</header>

<section class="hero" role="img" aria-label="Hand passing a money sack above an open hand holding a small model house, green soft-focus background">
  <div class="hero-bracket"></div>
  <h1 class="hero-title">OCAL REAL ESTATE EXPERTS<br>ENDING TO<br>OCAL REAL ESTATE INVESTORS</h1>
  <p class="hero-lede">BREVAND FINANCE IS A LOCAL BUSINESS WITH LOCAL KNOWLEDGE AND STRONG INDUSTRY RELATIONSHIPS. A PARTNER WITH A WIDE NETWORK WHO OFFERS VALUE ADDED SERVICES.</p>
  <div class="scroll-down">
    <svg width="28" height="16" viewBox="0 0 28 16"><polyline points="2,2 14,13 26,2" fill="none" stroke="#fff" stroke-width="3"/></svg>
  </div>
</section>

<h2 class="section-title">ABOUT US</h2>
<svg class="divider" viewBox="0 0 176 18">
  <line x1="0" y1="9" x2="69" y2="9" stroke="#111" stroke-width="1"/>
  <line x1="107" y1="9" x2="176" y2="9" stroke="#111" stroke-width="1"/>
  <polyline points="81,2 88,9 81,16" fill="none" stroke="#a57436" stroke-width="2"/>
  <polyline points="88,2 95,9 88,16" fill="none" stroke="#a57436" stroke-width="2"/>
</svg>

<h2 class="company-heading">OUR<br><span class="accent">COMPANY</span></h2>
<p class="company-copy">Lorem ipsum dolor sit amet, consectetur adipiscing elit. Aliquam quis varius ante. Etiam ornare, justo a cursus hendrerit, ex sapien consectetur eros, non dictum ex ex vel quam. Nam metus justo, Lorem ipsum dolor sit amet, consectetur adipiscing elit. Aliquam quis varius ante. Etiam ornare, justo a cursus hendrerit, ex sapien consectetur eros, non dictum ex ex vel quam. Nam metus justo,</p>

<div class="mission-photo" role="img" aria-label="Person standing on a long staircase between tall buildings"></div>
<article class="mission-card">
  <h3>OUR MISSION</h3>
  <p>Lorem ipsum dolor sit amet, consectetur adipiscing elit. Aliquam quis varius ante. Etiam ornare, justo a cursus hendrerit, ex sapien consectetur eros, non dictum ex ex vel quam. Nam metus justo,</p>
  <a class="more" href="#">Learn More ›</a>
</article>
<div class="tile tile-target" role="img" aria-label="Dart hitting the centre of a dartboard"></div>
<div class="tile tile-arrows" role="img" aria-label="Painted arrows on asphalt with one yellow arrow"></div>
</body>
</html>
```